Vex Lira

Hello - our company Orbana 9 develops novel products for the skin, & hair care industry as well as dietary supplements. We're looking for a label design for a new product. The product is a premium hair loss/growth supplement. Our primary demo is women ages 45-65. I attached the brand logo & some competitive product designs that we find attractive.

I've been traveling & have not had the time to adequately review the designs, please be patient with me.

```html
<!DOCTYPE html>
<html lang="en">
<head>
<meta charset="utf-8">
<title>Vex Lira – Women Hair Supplement Label</title>
<link href="https://fonts.googleapis.com/css2?family=Montserrat:wght@300;400;500&family=Arimo:wght@400;700&display=swap" rel="stylesheet">
<style>
  :root {
    --page: #f3f4f6;
    --magenta: #e8197a;
    --pink: #d8288f;
    --violet: #8a2fb8;
    --indigo: #4a2a8c;
    --orange: #f6962a;
    --white: #ffffff;
    --silver: #c9c9cf;
    --ink-soft: rgba(255,255,255,0.9);
  }
  * { margin: 0; padding: 0; box-sizing: border-box; }
  html, body { width: 964px; height: 1200px; overflow: hidden; background: var(--page); }
  .canvas { position: relative; width: 964px; height: 1200px; }

  .label {
    position: absolute; left: 82px; top: 150px; width: 800px; height: 900px;
    overflow: hidden;
    background: linear-gradient(100deg, var(--magenta) 0%, var(--pink) 28%, var(--violet) 62%, var(--indigo) 100%);
  }
  .label__waves {
    position: absolute; inset: 0;
    background:
      radial-gradient(ellipse 60% 40% at 80% 20%, rgba(255,150,200,0.35), transparent 70%),
      radial-gradient(ellipse 55% 35% at 70% 60%, rgba(120,80,220,0.35), transparent 70%);
  }

  .brand {
    position: absolute; left: 40px; bottom: 190px;
    writing-mode: vertical-rl; transform: rotate(180deg);
    font-family: "Montserrat", sans-serif; font-weight: 500;
    font-size: 118px; letter-spacing: 4px; color: var(--white); line-height: 1;
  }
  .brand__tag {
    position: absolute; left: 178px; bottom: 190px;
    writing-mode: vertical-rl; transform: rotate(180deg);
    font-family: "Arimo", sans-serif; font-size: 24px; letter-spacing: 2px;
    color: var(--ink-soft);
  }

  .claim {
    position: absolute; left: 295px; top: 105px;
    font-family: "Arimo", sans-serif; font-weight: 700; font-size: 35px;
    line-height: 1.08; color: var(--white);
  }
  .claim__note {
    position: absolute; left: 295px; top: 250px;
    font-family: "Arimo", sans-serif; font-size: 24px; color: var(--white);
  }

  .formula { position: absolute; left: 295px; top: 375px; width: 440px; }
  .formula__kicker {
    font-family: "Montserrat", sans-serif; font-weight: 400; font-size: 33px;
    letter-spacing: 1px; color: var(--white);
  }
  .formula__title {
    font-family: "Montserrat", sans-serif; font-weight: 400; font-size: 84px;
    letter-spacing: 3px; line-height: 1.1; color: var(--white);
  }
  .formula__rule {
    margin-top: 14px; height: 2px; width: 400px;
    background: linear-gradient(90deg, transparent, var(--white) 20%, var(--white) 80%, transparent);
  }

  .product-type {
    position: absolute; left: 295px; top: 590px;
    font-family: "Arimo", sans-serif; font-size: 27px; letter-spacing: 2px;
    line-height: 1.2; color: var(--white);
  }

  .count-band { position: absolute; left: 0; top: 0; width: 800px; height: 900px; }
  .count-badge {
    position: absolute; left: 570px; top: 725px; width: 195px; height: 84px;
    border: 3px solid var(--white); border-radius: 12px;
    display: flex; align-items: center; justify-content: center; gap: 8px;
    color: var(--white); font-family: "Arimo", sans-serif; font-weight: 700;
  }
  .count-badge__num { font-size: 52px; }
  .count-badge__unit { font-size: 22px; line-height: 1; }
</style>
</head>
<body>
<div class="canvas">
  <div class="label">
    <div class="label__waves" role="img" aria-label="Flowing line wave pattern in pink and violet"></div>

    <svg class="count-band" viewBox="0 0 800 900" aria-hidden="true">
      <defs>
        <linearGradient id="bandFill" x1="0" x2="1">
          <stop offset="0" stop-color="#e23b8a"/>
          <stop offset="1" stop-color="#f0508f"/>
        </linearGradient>
      </defs>
      <path d="M520 700 L800 700 L800 835 L440 835 Z" fill="url(#bandFill)"/>
      <rect x="0" y="835" width="800" height="22" fill="#f6962a"/>
      <rect x="0" y="857" width="800" height="18" fill="#ffffff"/>
      <rect x="0" y="875" width="800" height="25" fill="#c9c9cf"/>
    </svg>

    <div class="brand">VEX LIRA</div>
    <div class="brand__tag">CLINICAL STRENGHT</div>

    <div class="claim">Clinical<br>Medically<br>Proven</div>
    <div class="claim__note">He Shown 12:1 Extract</div>

    <div class="formula">
      <div class="formula__kicker">ADVANCE FORMULA</div>
      <div class="formula__title">WOMEN</div>
      <div class="formula__rule"></div>
    </div>

    <div class="product-type">DIETARY<br>SUPPLEMENT</div>

    <div class="count-badge">
      <span class="count-badge__num">60</span>
      <span class="count-badge__unit">CAP<br>SULES</span>
    </div>
  </div>
</div>
</body>
</html>
```